Packaging box design for health supplement

We need a design for our new health supplement product called "Lumoria Vitalis". We need design that is clean and will emphasize on Kiwifruit itself, so Green color should be present. This box should be able to contain 6 blister packs (10 capsules/blister pack). Measurement per blister pack is Length 55mm Width 8mm Height 72mm (pls estimate an allowance to fit all 6 blisters in the box you will design). I attached here the description and other information needed. I also attached here example of existing product in the market just to give you idea (although it is not in a box but in plastic bottle). Designer should provide measurements and cutting diagram on how the paper box will be assembled and cut for manufacturer reference.

```html
<!DOCTYPE html>
<html lang="en">
<head>
<meta charset="utf-8">
<title>Lumoria Vitalis – Carton Dieline</title>
<link href="https://fonts.googleapis.com/css2?family=Open+Sans:wght@300;400;600;700;800&family=Roboto:wght@300;400;700;900&family=Roboto+Condensed:wght@400;700&display=swap" rel="stylesheet">
<style>
  :root{
    --green:#3aa935;
    --green-dark:#1f8a3a;
    --green-light:#8cc63f;
    --lime:#d4df2a;
    --lime-soft:#e6ef7a;
    --kiwi-core:#f3f7c8;
    --ink:#222;
    --grey-box:#e6e7e8;
    --cut:#3a3a3a;
    --silver-a:#f4f4f4;
    --silver-b:#a9a9a9;
    --gold:#a8843e;
  }
  *{box-sizing:border-box;margin:0;padding:0}
  html,body{width:1200px;height:1000px;overflow:hidden;background:#fff}
  body{position:relative;font-family:"Open Sans",Arial,sans-serif;color:var(--ink)}
  .dieline{position:absolute;left:0;top:0}
  .abs{position:absolute}

  .brand{font-family:"Roboto",Arial,sans-serif;font-weight:900;color:var(--green);letter-spacing:-.3px}
  .brand-rule{height:2px;background:var(--green)}

  .kiwi-art{background:radial-gradient(ellipse at 50% 100%,var(--kiwi-core) 0 18%,var(--lime-soft) 30%,var(--green-light) 62%,#b9dc55 80%,#e3efa4 100%);
    border-radius:50% 50% 0 0 / 100% 100% 0 0}
  .kiwi-slices{border-radius:50%;background:radial-gradient(circle,var(--kiwi-core) 0 25%,var(--green-light) 55%,var(--green) 100%)}

  .title-band{background:linear-gradient(90deg,var(--green-dark),var(--green) 45%,#7cc242);color:#fff;text-align:center}
  .title{font-family:"Open Sans",Arial,sans-serif;line-height:1;white-space:nowrap}
  .title .light{font-weight:300}
  .title .bold{font-weight:700}
  .subtitle{font-weight:400;line-height:1;text-align:right;white-space:nowrap}
  .origin-band{background:var(--lime);color:#1d3a1d;font-weight:700;text-align:center;letter-spacing:1.4px;white-space:nowrap}
  .silver{background:linear-gradient(90deg,var(--silver-b),var(--silver-a) 20%,var(--silver-b) 45%,var(--silver-a) 70%,var(--silver-b))}

  .claim{color:var(--green);font-weight:700;font-size:8px;text-align:center;white-space:nowrap}
  .benefits{list-style:none;font-family:"Roboto Condensed","Arial Narrow",sans-serif;font-size:6.4px;line-height:11px;width:140px;overflow:hidden}
  .benefits li{display:flex;align-items:center;gap:3px;white-space:nowrap}
  .benefits svg{width:7px;height:7px;flex:none}
  .count-pill{background:var(--green);color:#fff;font-family:"Roboto Condensed","Arial Narrow",sans-serif;font-weight:700;font-size:6.4px;border-radius:8px;text-align:center;line-height:13px;white-space:nowrap}

  .info{font-family:"Roboto Condensed","Arial Narrow",sans-serif;font-size:6.6px;line-height:9.4px}
  .info h4{font-weight:700;font-size:6.6px}
  .info p{margin-bottom:4px}
  .placeholder-box{background:var(--grey-box)}
  .copy{font-family:"Roboto Condensed","Arial Narrow",sans-serif;font-size:6.5px;line-height:9.8px;text-align:justify}
  .seal{background:var(--gold);clip-path:polygon(50% 0,100% 25%,100% 75%,50% 100%,0 75%,0 25%)}
  .note{font-family:"Roboto Condensed","Arial Narrow",sans-serif;font-size:6.6px;line-height:9px}

  .flipped{transform:rotate(180deg);transform-origin:center}
</style>
</head>
<body>

<svg class="dieline" width="1200" height="1000" viewBox="0 0 1200 1000" aria-hidden="true">
  <g fill="none" stroke="var(--cut)" stroke-width="1">
    <path d="M48,230 V18 Q48,0 66,0 H240 Q258,0 258,18 V230" fill="var(--lime)"/>
    <rect x="48" y="30" width="210" height="200" fill="#fff" stroke="none"/>
    <path d="M48,30 V230 M258,30 V230"/>
    <line x1="28" y1="40" x2="282" y2="40"/>
    <path d="M48,230 L10,245 V490 L48,500"/>
    <path d="M262,230 V105 H400 L438,195 L448,210 V230"/>
    <path d="M658,230 V210 L668,195 L690,105 H848 V230"/>
    <path d="M848,210 L855,215 V495 L848,500"/>
    <path d="M262,500 L275,525 V625 H435 L448,510 V500"/>
    <path d="M658,500 L670,525 V625 H830 L848,510 V500"/>
    <path d="M448,500 V712 Q448,730 466,730 H640 Q658,730 658,712 V500" fill="var(--lime)"/>
    <rect x="448" y="500" width="210" height="190" fill="#fff" stroke="none"/>
    <path d="M448,500 V690 M658,500 V690"/>
    <line x1="28" y1="230" x2="860" y2="230"/>
    <line x1="28" y1="500" x2="860" y2="500"/>
    <line x1="258" y1="230" x2="258" y2="500"/>
    <line x1="448" y1="105" x2="448" y2="500"/>
    <line x1="658" y1="105" x2="658" y2="500"/>
    <line x1="848" y1="230" x2="848" y2="500"/>
  </g>
</svg>

<!-- top tuck artwork (upside down) -->
<section class="abs flipped" style="left:48px;top:30px;width:210px;height:200px" aria-label="Top tuck flap">
  <div class="abs brand" style="left:6px;top:2px;font-size:14px">Verdanta®</div>
  <div class="abs brand-rule" style="left:84px;top:10px;width:126px"></div>
  <div class="abs kiwi-art" role="img" aria-label="Kiwifruit slice illustration" style="left:8px;top:30px;width:194px;height:70px"></div>
  <div class="abs title-band" style="left:0;top:100px;width:210px;height:40px">
    <div class="title" style="font-size:19px;padding-top:6px"><span class="light">LUMORIA</span><span class="bold">VITALIS</span></div>
    <div class="subtitle" style="font-size:10px;padding-right:24px">with Fibrelle®</div>
  </div>
  <div class="abs origin-band" style="left:0;top:140px;width:210px;height:15px;font-size:7.5px;line-height:15px;background:#fff;color:var(--ink)">PRODUCT OF NEW ZEALAND</div>
  <div class="abs origin-band" style="left:0;top:160px;width:210px;height:14px;font-size:6.2px;line-height:14px;color:var(--green-dark)">60 CAPSULES IN BLISTER PACK</div>
</section>

<!-- front panel 1 -->
<section class="abs" style="left:48px;top:230px;width:210px;height:270px" aria-label="Front panel">
  <div class="abs brand" style="left:10px;top:10px;font-size:14px">Verdanta®</div>
  <div class="abs brand-rule" style="left:90px;top:18px;width:120px"></div>
  <div class="abs kiwi-art" role="img" aria-label="Kiwifruit slice illustration" style="left:0;top:38px;width:210px;height:82px"></div>
  <div class="abs title-band" style="left:0;top:118px;width:210px;height:44px">
    <div class="title" style="font-size:19.5px;padding-top:6px"><span class="light">LUMORIA</span><span class="bold">VITALIS</span></div>
    <div class="subtitle" style="font-size:10px;padding-right:26px">with Fibrelle®</div>
  </div>
  <div class="abs origin-band" style="left:0;top:162px;width:210px;height:16px;font-size:7.6px;line-height:16px">PRODUCT OF NEW ZEALAND</div>
  <div class="abs claim" style="left:0;top:180px;width:210px">Helps Maintain Healthy Weight &amp; Digestion.</div>
  <div class="abs kiwi-slices" role="img" aria-label="Kiwifruit slices illustration" style="left:10px;top:196px;width:46px;height:46px"></div>
  <ul class="abs benefits" style="left:64px;top:194px">
    <li><svg viewBox="0 0 8 8"><path d="M1,4 L3.2,6.2 L7,1.5" fill="none" stroke="var(--green)" stroke-width="1.6"/></svg>Delivers more soluble fiber that controls weight</li>
    <li><svg viewBox="0 0 8 8"><path d="M1,4 L3.2,6.2 L7,1.5" fill="none" stroke="var(--green)" stroke-width="1.6"/></svg>Higher level of digestive enzymes</li>
    <li><svg viewBox="0 0 8 8"><path d="M1,4 L3.2,6.2 L7,1.5" fill="none" stroke="var(--green)" stroke-width="1.6"/></svg>Improves digestion of heavy proteins</li>
    <li><svg viewBox="0 0 8 8"><path d="M1,4 L3.2,6.2 L7,1.5" fill="none" stroke="var(--green)" stroke-width="1.6"/></svg>Increase the level of good bacteria</li>
  </ul>
  <div class="abs count-pill" style="left:104px;top:245px;width:102px">60 CAPSULES IN BLISTER PACK</div>
  <div class="abs silver" style="left:0;top:260px;width:210px;height:10px"></div>
</section>

<!-- side panel 2: ingredients -->
<section class="abs" style="left:258px;top:230px;width:190px;height:270px" aria-label="Ingredients side panel">
  <div class="abs title-band" style="left:0;top:10px;width:190px;height:42px">
    <div class="title" style="font-size:17px;padding-top:6px"><span class="light">LUMORIA</span><span class="bold">VITALIS</span></div>
    <div class="subtitle" style="font-size:9.5px;padding-right:12px">with Fibrelle®</div>
  </div>
  <div class="abs info" style="left:12px;top:56px;width:168px">
    <h4>Ingredients:</h4>
    <p>Fibrelle®Lumoria Vitalis ..........................400mg<br>KiwifruitSkin Extract.......................................100mg</p>
    <h4>Directions:</h4>
    <p>Take 1 to 2 capsules daily.</p>
    <h4>Warning:</h4>
    <p>People who are allergic to kiwifruit may also be allergic to this product.</p>
    <h4>Manufactured by:</h4>
    <p>Verdanta<br>address /contery. state/ code<br>contact information no.<br>email/ website</p>
  </div>
  <div class="abs placeholder-box" style="left:10px;top:205px;width:170px;height:52px"></div>
  <div class="abs silver" style="left:0;top:260px;width:190px;height:10px"></div>
</section>

<!-- front panel 3 -->
<section class="abs" style="left:448px;top:230px;width:210px;height:270px" aria-label="Back front panel">
  <div class="abs brand" style="left:10px;top:10px;font-size:14px">Verdanta®</div>
  <div class="abs brand-rule" style="left:90px;top:18px;width:120px"></div>
  <div class="abs kiwi-art" role="img" aria-label="Kiwifruit slice illustration" style="left:0;top:38px;width:210px;height:82px"></div>
  <div class="abs title-band" style="left:0;top:118px;width:210px;height:44px">
    <div class="title" style="font-size:19.5px;padding-top:6px"><span class="light">LUMORIA</span><span class="bold">VITALIS</span></div>
    <div class="subtitle" style="font-size:10px;padding-right:26px">with Fibrelle®</div>
  </div>
  <div class="abs origin-band" style="left:0;top:162px;width:210px;height:16px;font-size:7.6px;line-height:16px">PRODUCT OF NEW ZEALAND</div>
  <div class="abs claim" style="left:0;top:180px;width:210px">Helps Maintain Healthy Weight &amp; Digestion.</div>
  <div class="abs kiwi-slices" role="img" aria-label="Kiwifruit slices illustration" style="left:10px;top:196px;width:46px;height:46px"></div>
  <ul class="abs benefits" style="left:64px;top:194px">
    <li><svg viewBox="0 0 8 8"><path d="M1,4 L3.2,6.2 L7,1.5" fill="none" stroke="var(--green)" stroke-width="1.6"/></svg>Delivers more soluble fiber that controls weight</li>
    <li><svg viewBox="0 0 8 8"><path d="M1,4 L3.2,6.2 L7,1.5" fill="none" stroke="var(--green)" stroke-width="1.6"/></svg>Higher level of digestive enzymes</li>
    <li><svg viewBox="0 0 8 8"><path d="M1,4 L3.2,6.2 L7,1.5" fill="none" stroke="var(--green)" stroke-width="1.6"/></svg>Improves digestion of heavy proteins</li>
    <li><svg viewBox="0 0 8 8"><path d="M1,4 L3.2,6.2 L7,1.5" fill="none" stroke="var(--green)" stroke-width="1.6"/></svg>Increase the level of good bacteria</li>
  </ul>
  <div class="abs count-pill" style="left:104px;top:245px;width:102px">60 CAPSULES IN BLISTER PACK</div>
  <div class="abs silver" style="left:0;top:260px;width:210px;height:10px"></div>
</section>

<!-- side panel 4: description -->
<section class="abs" style="left:658px;top:230px;width:190px;height:270px" aria-label="Description side panel">
  <div class="abs title-band" style="left:0;top:10px;width:190px;height:42px">
    <div class="title" style="font-size:17px;padding-top:6px"><span class="light">LUMORIA</span><span class="bold">VITALIS</span></div>
    <div class="subtitle" style="font-size:9.5px;padding-right:12px">with Fibrelle®</div>
  </div>
  <div class="abs copy" style="left:8px;top:58px;width:174px">
    <p>Verdanta Lumoria Vitalis contains Fibrelle® a proprietary formulation that uses whole Kiwifruit including skin, seeds and flesh. Unlike other kiwifruit powders, which only use the kiwifruit flesh.</p>
    <p>This Lumoria Vitalis delivers more soluble fibre which delays the emptying of your stomach and makes you feel full, which helps control weight. Higher level of digestive enzymes activities also ensures that heavy proteins like meat, milk and tofu are digested well and help your body break down the nutrients from food. This special formulation also act as a powerful prebiotic, increasing the level of good bacteria maintaining a healthy digestive system.</p>
  </div>
  <div class="abs seal" role="img" aria-label="Origin certification seal" style="left:10px;top:188px;width:70px;height:66px"></div>
  <div class="abs note" style="left:97px;top:214px;width:80px">other infor mation regarding safety. and product care</div>
</section>

<!-- enlarged front artwork detail -->
<section class="abs" style="left:50px;top:670px;width:380px;height:315px" aria-label="Front artwork detail">
  <div class="abs brand" style="left:18px;top:6px;font-size:25px">Verdanta®</div>
  <div class="abs brand-rule" style="left:168px;top:21px;width:212px"></div>
  <div class="abs kiwi-art" role="img" aria-label="Kiwifruit slice illustration" style="left:0;top:50px;width:380px;height:148px"></div>
  <div class="abs title-band" style="left:0;top:195px;width:380px;height:90px">
    <div class="title" style="font-size:37px;padding-top:13px"><span class="light">LUMORIA</span><span class="bold">VITALIS</span></div>
    <div class="subtitle" style="font-size:20px;padding-right:30px;padding-top:2px">with Fibrelle®</div>
  </div>
  <div class="abs origin-band" style="left:0;top:285px;width:380px;height:30px;font-size:14px;line-height:30px;letter-spacing:2.6px">PRODUCT OF NEW ZEALAND</div>
</section>

</body>
</html>
```